Business Card Design for a Sound engineer and DJ

We would like a residn of the business card.

Logo must remain the same.
The card is for the owner of the company.
The business card is in Arabic as the company is based in Kuwait.
The company specializes in sound engineering for singers concerts and events and in addition DJ.
The color options is up to the designer but we would like it masculine as the owner is a man.

Target Market(s)

All ages

Industry/Entity Type

Media

Contact Information for Business Card

Name:
Eng. Tarek Halabi
م/طارق حلبي

The name above is in Arabic and English.

Title: General Manager
Mobile: +965 66307852
Office: +965 22486037
Email: info@sawtarin.net

Address:
Office no. 3
1st floor
Almarfa Complex
Rashed AlQeblawi St.
Salmiya
Kuwait

Instagram: @sawtarin
Snap: sawtarin

Requirements
Nice to have
• can we have Instagram icon and snap icon and a phone vector and email?
• Instead of writing the words

```html
<!DOCTYPE html>
<html lang="en">
<head>
<meta charset="utf-8">
<title>Sawtarin – Business Card</title>
<link rel="stylesheet" href="https://fonts.googleapis.com/css2?family=Arimo:wght@400;700&family=Cairo:wght@400;600&display=swap">
<style>
  :root {
    --night: #05051c;
    --deep-blue: #1a1aa8;
    --violet: #4a1fd6;
    --purple: #7a2ee0;
    --magenta: #e11ee6;
    --logo-frame: #f02ef0;
    --logo-ink: #7d3fd8;
    --paper: #ffffff;
    --ink-light: #ffffff;
    --ink-soft: #e8e8ff;
  }
  html, body {
    margin: 0;
    padding: 0;
    width: 1200px;
    height: 720px;
    overflow: hidden;
    background: var(--night);
  }
  .card {
    position: relative;
    width: 1200px;
    height: 720px;
    overflow: hidden;
    font-family: "Arimo", Arial, sans-serif;
    color: var(--ink-light);
  }
  .card__backdrop {
    position: absolute;
    inset: 0;
    background:
      radial-gradient(ellipse 520px 380px at 230px 230px, rgba(90, 60, 255, 0.85), transparent 70%),
      radial-gradient(ellipse 420px 300px at 1150px 80px, rgba(70, 50, 230, 0.7), transparent 70%),
      radial-gradient(ellipse 500px 260px at 420px 560px, rgba(40, 40, 170, 0.6), transparent 75%),
      linear-gradient(160deg, var(--deep-blue) 0%, #0c0c4a 45%, var(--night) 75%, #0a0a30 100%);
  }
  .brand {
    position: absolute;
    left: 146px;
    top: 67px;
    width: 351px;
    height: 354px;
    box-sizing: border-box;
    border: 6px solid var(--logo-frame);
    border-radius: 30px;
    padding: 10px;
  }
  .brand__tile {
    width: 100%;
    height: 100%;
    background: var(--paper);
    border-radius: 20px;
    display: flex;
    flex-direction: column;
    align-items: center;
    justify-content: center;
    gap: 10px;
  }
  .brand__mark {
    width: 34px;
    height: 34px;
    background: var(--logo-ink);
    border-radius: 50%;
  }
  .brand__name {
    font-family: "Arimo", Arial, sans-serif;
    font-weight: 700;
    font-size: 44px;
    letter-spacing: 4px;
    color: var(--logo-ink);
    margin: 0;
  }
  .brand__tagline {
    font-weight: 700;
    font-size: 14px;
    letter-spacing: 1.5px;
    color: var(--logo-ink);
    margin: 0;
  }
  .brand__tagline-ar {
    font-family: "Cairo", sans-serif;
    font-weight: 600;
    font-size: 16px;
    color: var(--logo-ink);
    margin: -6px 0 0;
  }
  .owner {
    position: absolute;
    left: 654px;
    top: 36px;
  }
  .owner__name-ar {
    font-family: "Cairo", sans-serif;
    font-size: 22px;
    margin: 0 0 4px 18px;
    direction: rtl;
    text-align: left;
    unicode-bidi: plaintext;
  }
  .owner__block {
    border-left: 5px solid;
    border-image: linear-gradient(var(--magenta), var(--purple)) 1;
    padding-left: 14px;
  }
  .owner__name {
    font-size: 34px;
    margin: 0;
    letter-spacing: -0.5px;
  }
  .owner__title {
    font-size: 21px;
    margin: 8px 0 0;
  }
  .contacts {
    position: absolute;
    left: 632px;
    top: 276px;
    margin: 0;
    padding: 0;
    list-style: none;
  }
  .contact {
    display: flex;
    align-items: center;
    gap: 14px;
    height: 38px;
    margin-bottom: 22px;
    font-size: 28px;
  }
  .contact--address {
    align-items: flex-start;
    height: auto;
    font-size: 21px;
    line-height: 29px;
  }
  .contact__icon {
    flex: none;
    width: 38px;
    height: 38px;
    border-radius: 9px;
    background: var(--magenta);
    display: flex;
    align-items: center;
    justify-content: center;
  }
  .contact__icon svg { width: 24px; height: 24px; fill: var(--ink-light); }
  .contact__address-lines { margin-top: 2px; }
</style>
</head>
<body>
  <main class="card">
    <div class="card__backdrop" role="img" aria-label="Photo of a DJ's hand adjusting knobs on a mixing console under blue and purple stage light"></div>

    <div class="brand">
      <div class="brand__tile">
        <span class="brand__mark"></span>
        <p class="brand__name">SAWTARIN</p>
        <p class="brand__tagline">DJ - SOUND ENG. - LIGHTING</p>
        <p class="brand__tagline-ar" lang="ar" dir="rtl">دي جي - هندسة صوت - إضاءة</p>
      </div>
    </div>

    <header class="owner">
      <p class="owner__name-ar" lang="ar">م/طارق حلبي</p>
      <div class="owner__block">
        <h1 class="owner__name">Eng. Tarek Halabi</h1>
        <p class="owner__title">G. Manager</p>
      </div>
    </header>

    <ul class="contacts">
      <li class="contact">
        <span class="contact__icon">
          <svg viewBox="0 0 24 24" aria-hidden="true"><path d="M6.6 10.8a15.1 15.1 0 0 0 6.6 6.6l2.2-2.2a1 1 0 0 1 1-.25 11.4 11.4 0 0 0 3.6.57 1 1 0 0 1 1 1V20a1 1 0 0 1-1 1A17 17 0 0 1 3 4a1 1 0 0 1 1-1h3.5a1 1 0 0 1 1 1c0 1.25.2 2.45.57 3.57a1 1 0 0 1-.25 1z"/></svg>
        </span>
        <span>+965 66 30 78 52</span>
      </li>
      <li class="contact">
        <span class="contact__icon">
          <svg viewBox="0 0 24 24" aria-hidden="true"><path d="M8 1h8a2 2 0 0 1 2 2v18a2 2 0 0 1-2 2H8a2 2 0 0 1-2-2V3a2 2 0 0 1 2-2zm0 3v14h8V4zm4 15.2a1.1 1.1 0 1 0 0 2.2 1.1 1.1 0 0 0 0-2.2z"/></svg>
        </span>
        <span>+965 22 48 60 37</span>
      </li>
      <li class="contact">
        <span class="contact__icon">
          <svg viewBox="0 0 24 24" aria-hidden="true"><path d="M2 5h20v14H2zm2 2v.4l8 5.3 8-5.3V7zm0 2.8V17h16V9.8l-8 5.3z"/></svg>
        </span>
        <span>tarekbeat@me.com</span>
      </li>
      <li class="contact">
        <span class="contact__icon">
          <svg viewBox="0 0 24 24" aria-hidden="true"><path d="M2 5h20v14H2zm2 2v.4l8 5.3 8-5.3V7zm0 2.8V17h16V9.8l-8 5.3z"/></svg>
        </span>
        <span>info@sawtarin.net</span>
      </li>
      <li class="contact contact--address">
        <span class="contact__icon">
          <svg viewBox="0 0 24 24" aria-hidden="true"><path d="M12 1a7.5 7.5 0 0 0-7.5 7.5C4.5 14.5 12 23 12 23s7.5-8.5 7.5-14.5A7.5 7.5 0 0 0 12 1zm0 10.2a2.7 2.7 0 1 1 0-5.4 2.7 2.7 0 0 1 0 5.4z"/></svg>
        </span>
        <span class="contact__address-lines">
          Kuwait-Salmiya-Rashed Al-Qeblawi St.<br>
          Al-Marfa Comp. 1st Floor - Office No. #3
        </span>
      </li>
    </ul>
  </main>
</body>
</html>
```